Pinecrest Real Estate A5 Flyer

A5 Flyer for print distribution.

Front (include attached photo and branding):
Pinecrest are a new face in the Shelley & Rossmoyne real estate market. The Pinecrest team are both Shelley ‘locals’ and are genuinely and sincerely committed to this community. They put people first and pursue exceptional outcomes for their clients. This is the founding vision of Pinecrest.

Values:
Outstanding Customer Service
Timely Communication
Integrity Always
People First
Exceptional Negotiation

If you’re thinking of selling, interested in a free market appraisal, or simply want to find out more about the Pinecrest team, please reach out to Doug or Rowan for a chat. We’d love to shout you a coffee at The Lantern Coffee + Kitchen.

Pinecrest Real Estate
E: hello@pinecrestrealestate-example.com.au
W: pinecrestrealestate-example.com.au

Back (half the page about Doug, other half the page about Rowan). Please include headshots (Rowan is the younger one):

Rowan Ferrabee (Property Consultant):

Rowan has an in-depth understanding of all things property & finance related. With a degree in property & finance, diploma in finance & mortgage broking, certificate IV in real estate practice, project management roles in residential property development, plus years of small business experience as co-founder/co-owner of The Lantern Coffee + Kitchen, his experience in managing competing demands and complex scenarios runs far and wide.

Rowan also has experience in corporate negotiations which is proving to be a very beneficial skill set. Rowan is deeply committed to people and pursuing exceptional outcomes for his clients. He has built a reputation as a man of his word who is genuine and sincere and willing to go above and beyond for his clients.

rowan@pinecrestrealestate-example.com.au
0412 306 248

Doug Penberthy (Director / Licensee):

Doug has worked in various roles inclusive of being a Real Estate Agent, Bank Manager, Financial Counsellor, Mortgage Broker, and previously a Commercial Pilot. He spent eight years in remote Western Australia, where he worked for an international mining company creating strategies to help support the well-being of employees. Doug’s focus in life has always been to help people. To him, it is always about the relationship. Doug gets enormous satisfaction from seeing individuals, families, and businesses thrive financially. He has become a skilled negotiator with extensive experience working for a number of corporations and private firms.
 
What differentiates Doug is his compassion and commitment to people. He works hard to be an excellent communicator with the aim of achieving great results. He  has extensive sales experience with incredible ability to push the boundaries, think outside the box and meet or surpass expectations. This is why his clients keep coming back and continue to refer well into the future. 

doug@pinecrestrealestate-example.com.au
0438 192 607

Target Market(s)

House Sellers / House Buyers

Industry/Entity Type

Real Estate

Colors
0054AA
0677BA
7BADD7
CADEEF
E8F1F8

Requirements
Must have
• Branding / logo, river photo, head shots, company details etc
Nice to have
• Design as per attached branding guide

```html
<!DOCTYPE html>
<html lang="en">
<head>
<meta charset="utf-8">
<title>Pinecrest Real Estate A5 Flyer</title>
<link rel="stylesheet" href="https://fonts.googleapis.com/css2?family=Poppins:wght@400;500;600;700&family=Libre+Baskerville:wght@400;700&display=swap">
<style>
:root{
  --navy:#16202e;
  --slate:#5b606d;
  --slate-light:#8a8e99;
  --rule:#c4c6cc;
  --paper:#ffffff;
  --ink:#1b2433;
  --backdrop:#c9c9c9;
  --photo-a:#7d93ad;
  --photo-b:#4d6688;
  --portrait-a:#c9ccd3;
  --portrait-b:#a9aeb8;
}
*{box-sizing:border-box;margin:0;padding:0}
html,body{width:788px;height:1200px;overflow:hidden}
body{background:var(--backdrop);font-family:"Poppins",sans-serif;color:var(--ink);position:relative}
.page{position:absolute;left:189px;width:410px;height:580px;background:var(--paper);overflow:hidden;box-shadow:0 6px 14px rgba(0,0,0,.28)}
.page--front{top:10px}
.page--back{top:610px}
.abs{position:absolute}

/* front */
.front__band{left:0;top:0;width:410px;height:127px;background:var(--navy)}
.brand{left:0;top:24px;width:410px;display:flex;justify-content:center;align-items:center;gap:8px}
.brand__dot{width:22px;height:22px;border-radius:50%;background:#e9eaec}
.brand__name{font-family:"Libre Baskerville",serif;font-size:15px;letter-spacing:5px;color:#e9eaec}
.hero{left:18px;top:61px;width:373px;height:198px;background:var(--paper);border:2px solid var(--navy);padding:3px}
.hero__photo{width:100%;height:100%;background:linear-gradient(180deg,var(--photo-a),var(--photo-b));border:2px solid var(--navy)}
.headline{left:10px;top:274px;width:390px;text-align:center;font-weight:700;font-size:14px;line-height:17px;color:var(--navy)}
.dots{left:182px;top:309px;display:flex;gap:2px}
.dots span{width:6px;height:4px;background:var(--slate)}
.dots span:first-child,.dots span:last-child{background:var(--slate-light)}
.intro{left:30px;top:321px;width:350px;text-align:center;font-size:8.6px;line-height:10.6px;color:var(--ink)}
.values{left:23px;top:365px;width:364px;height:88px;display:flex}
.value{flex:1;display:flex;flex-direction:column;align-items:center;padding-top:27px;color:#fff;text-align:center;font-family:"Libre Baskerville",serif;font-size:5.6px;line-height:6.6px;text-transform:uppercase}
.value--dark{background:linear-gradient(180deg,#2a3342,var(--navy))}
.value--mid{background:linear-gradient(180deg,#777b87,#555a67)}
.value__icon{width:22px;height:22px;border-radius:50%;background:#fff;border:2px solid #cfd1d6;margin-bottom:8px;display:flex;align-items:center;justify-content:center}
.values__tab{left:131px;top:357px;width:148px;height:26px}
.values__tab-label{left:131px;top:359px;width:148px;text-align:center;color:#fff;font-weight:700;font-size:14px;letter-spacing:.5px}
.cta-text{left:23px;top:463px;width:166px;font-size:9.4px;line-height:11.6px;color:var(--ink)}
.cta-box{left:192px;top:461px;width:195px;height:58px;border:1.4px solid var(--navy);border-radius:4px;padding:7px 10px}
.cta-box__kicker{font-size:7.6px;font-weight:500;line-height:9px}
.cta-box__title{font-size:9.4px;font-weight:700;line-height:11px;color:var(--navy);padding-bottom:3px;border-bottom:1px solid var(--rule);margin-bottom:4px}
.cta-box__note{font-size:7px;line-height:8.4px}
.cta-box__tail{left:360px;top:517px}

/* footer */
.footer{left:0;top:533px;width:410px;height:47px}
.footer__name{left:23px;top:556px;font-family:"Libre Baskerville",serif;font-weight:700;font-size:11.4px;color:#fff;letter-spacing:.2px}
.footer__contacts{left:244px;top:537px;font-size:6.8px;line-height:9.6px;font-weight:600;color:var(--ink)}
.footer__contacts div{display:flex;align-items:center;gap:4px}
.footer__contacts svg{flex:none}

/* back */
.back__band{left:0;top:0;width:410px;height:255px;background:var(--navy)}
.back__rule{left:0;top:258px;width:410px;height:6px;background:linear-gradient(90deg,#6d717c,#9a9ea8)}
.headshot{border-radius:50%;border:3px solid #fff;box-shadow:0 0 0 2px var(--navy)}
.headshot__photo{width:100%;height:100%;border-radius:50%;background:linear-gradient(180deg,var(--portrait-a),var(--portrait-b))}
.headshot--rowan{left:23px;top:39px;width:114px;height:114px}
.headshot--doug{left:275px;top:315px;width:112px;height:112px}
.nameplate{font-family:"Libre Baskerville",serif;font-weight:700;font-size:15px;line-height:21px;padding:0 6px;color:#fff;border:1px solid #c9cbd1;background:linear-gradient(180deg,#7a7e89,#555a66)}
.nameplate--rowan{left:148px;top:31px}
.nameplate--doug{left:23px;top:276px;border-color:var(--navy);background:linear-gradient(180deg,#2f3847,#16202e)}
.role{font-weight:700;font-size:10.4px;padding-bottom:3px;border-bottom:1px solid #9a9ea8}
.role--rowan{left:148px;top:57px;width:233px;color:#fff}
.role--doug{left:23px;top:301px;width:227px;color:var(--navy)}
.bio{font-size:7.55px;line-height:9.35px}
.bio--light{color:#eef0f3}
.bio--rowan-1{left:148px;top:84px;width:236px}
.bio--rowan-2{left:23px;top:166px;width:366px}
.bio--doug-1{left:23px;top:328px;width:245px;color:var(--ink)}
.bio--doug-2{left:23px;top:436px;width:366px;color:var(--ink)}
.pill{display:flex;align-items:center;gap:4px;height:18px;padding:0 7px 0 2px;border-radius:3px;font-size:9px;font-weight:500;color:#fff}
.pill--onnavy{background:#343d4c}
.pill--onwhite{background:#3a4352}
.pill__icon{width:15px;height:15px;border-radius:50%;background:#fff;display:flex;align-items:center;justify-content:center;flex:none}
.contact-row{display:flex;gap:10px}
.contact-row--rowan{left:23px;top:216px}
.contact-row--doug{left:23px;top:496px}
</style>
</head>
<body>

<section class="page page--front">
  <div class="abs front__band"></div>
  <div class="abs brand"><span class="brand__dot"></span><span class="brand__name">PINECREST</span></div>
  <div class="abs hero"><div class="hero__photo" role="img" aria-label="Aerial photo of the Swan River foreshore at Shelley and Rossmoyne with the city skyline in the distance"></div></div>
  <h1 class="abs headline">PINECREST ARE A NEW FACE IN THE SHELLEY<br>&amp; ROSSMOYNE REAL ESTATE MARKET</h1>
  <div class="abs dots"><span></span><span></span><span></span><span></span><span></span></div>
  <p class="abs intro">The Pinecrest team are both Shelley ‘locals’ and are genuinely and sincerely committed to this community. They put people first and pursue exceptional outcomes for their clients. This is the founding vision of Pinecrest.</p>

  <div class="abs values">
    <div class="value value--dark"><span class="value__icon"><svg width="12" height="12" viewBox="0 0 12 12"><circle cx="6" cy="4" r="2" fill="#16202e"/><path d="M2 11c0-3 2-4 4-4s4 1 4 4z" fill="#16202e"/></svg></span>Outstanding<br>Customer<br>Service</div>
    <div class="value value--mid"><span class="value__icon"><svg width="12" height="12" viewBox="0 0 12 12"><rect x="1" y="2" width="10" height="7" rx="1.5" fill="#16202e"/><path d="M3 9l-1 3 3-3z" fill="#16202e"/></svg></span>Timely<br>Communication</div>
    <div class="value value--dark"><span class="value__icon"><svg width="12" height="12" viewBox="0 0 12 12"><path d="M6 1l4.5 2v3c0 3-2 4.5-4.5 5.5C3.5 10.5 1.5 9 1.5 6V3z" fill="#16202e"/><path d="M3.8 6l1.6 1.6L8.4 4.6" stroke="#fff" stroke-width="1.2" fill="none"/></svg></span>Integrity<br>Always</div>
    <div class="value value--mid"><span class="value__icon"><svg width="12" height="12" viewBox="0 0 12 12"><circle cx="6" cy="4.5" r="3" fill="none" stroke="#16202e" stroke-width="1.4"/><path d="M1 11h10" stroke="#16202e" stroke-width="1.6"/></svg></span>People First</div>
    <div class="value value--dark"><span class="value__icon"><svg width="12" height="12" viewBox="0 0 12 12"><circle cx="6" cy="6" r="4.5" fill="#16202e"/><path d="M3.6 6.2l1.6 1.6 3.2-3.4" stroke="#fff" stroke-width="1.2" fill="none"/></svg></span>Exceptional<br>Negotiation</div>
  </div>
  <svg class="abs values__tab" viewBox="0 0 148 26"><path d="M0 0H148L130 26H18Z" fill="#7d818c"/><path d="M0 0H148" stroke="#b9bcc3" stroke-width="2"/></svg>
  <div class="abs values__tab-label">VALUES</div>

  <p class="abs cta-text">If you’re thinking of selling, interested in a free market appraisal, or simply want to find out more about the Pinecrest team</p>
  <div class="abs cta-box">
    <div class="cta-box__kicker">PLEASE REACH OUT TO</div>
    <div class="cta-box__title">DOUG OR ROWAN FOR A CHAT</div>
    <div class="cta-box__note">We’d love to shout you a coffee at The<br>Lantern Coffee + Kitchen</div>
  </div>
  <svg class="abs cta-box__tail" width="14" height="10" viewBox="0 0 14 10"><path d="M0 0L7 9L13 0" fill="#fff" stroke="#16202e" stroke-width="1.4"/></svg>

  <svg class="abs footer" viewBox="0 0 410 47"><path d="M0 0H211L236 28H410V47H0Z" fill="#16202e"/><path d="M214 0L239 25H410" stroke="#9a9ea8" stroke-width="1.5" fill="none"/></svg>
  <div class="abs footer__name">PINECREST REAL ESTATE</div>
  <div class="abs footer__contacts">
    <div><svg width="7" height="5" viewBox="0 0 7 5"><rect x=".3" y=".3" width="6.4" height="4.4" fill="none" stroke="#555" stroke-width=".6"/><path d="M.3.3L3.5 3 6.7.3" fill="none" stroke="#555" stroke-width=".6"/></svg>hello@pinecrestrealestate-example.com.au</div>
    <div><svg width="7" height="7" viewBox="0 0 7 7"><circle cx="3.5" cy="3.5" r="3" fill="none" stroke="#555" stroke-width=".6"/><path d="M.5 3.5h6M3.5.5v6" stroke="#555" stroke-width=".5"/></svg>pinecrestrealestate-example.com.au</div>
  </div>
</section>

<section class="page page--back">
  <div class="abs back__band"></div>
  <div class="abs back__rule"></div>

  <div class="abs headshot headshot--rowan"><div class="headshot__photo" role="img" aria-label="Headshot of Rowan Ferrabee, property consultant"></div></div>
  <div class="abs nameplate nameplate--rowan">ROWAN FERRABEE</div>
  <div class="abs role role--rowan">PROPERTY CONSULTANT</div>
  <p class="abs bio bio--light bio--rowan-1">Rowan has an in-depth understanding of all things property &amp; finance related. With a degree in property &amp; finance, diploma in finance &amp; mortgage broking, certificate IV in real estate practice, project management roles in residential property development, plus years of small business experience as co-founder/co-owner of The Lantern Coffee + Kitchen, his experience in managing competing demands and complex scenarios runs far and wide.</p>
  <p class="abs bio bio--light bio--rowan-2">Rowan also has experience in corporate negotiations which is proving to be a very beneficial skill set. Rowan is deeply committed to people and pursuing exceptional outcomes for his clients. He has built a reputation as a man of his word who is genuine and sincere and willing to go above and beyond for his clients.</p>
  <div class="abs contact-row contact-row--rowan">
    <span class="pill pill--onnavy"><span class="pill__icon"><svg width="9" height="9" viewBox="0 0 9 9"><path d="M2 .8l1.4 1.8-.8 1c.5 1 1.3 1.8 2.3 2.3l1-.8L7.7 6.5 7 8C4 8 1 5 1 2z" fill="#16202e"/></svg></span>0412 306 248</span>
    <span class="pill pill--onnavy"><span class="pill__icon"><svg width="9" height="7" viewBox="0 0 9 7"><rect x=".5" y=".5" width="8" height="6" fill="#16202e"/><path d="M.5.5L4.5 4 8.5.5" fill="none" stroke="#fff" stroke-width=".8"/></svg></span>rowan@pinecrestrealestate-example.com.au</span>
  </div>

  <div class="abs nameplate nameplate--doug">DOUG PENBERTHY</div>
  <div class="abs role role--doug">DIRECTOR / LICENSEE</div>
  <p class="abs bio bio--doug-1">Doug has worked in various roles inclusive of being a Real Estate Agent, Bank Manager, Financial Counsellor, Mortgage Broker, and previously a Commercial Pilot. He spent eight years in remote Western Australia, where he worked for an international mining company creating strategies to help support the well-being of employees. Doug’s focus in life has always been to help people. To him, it is always about the relationship. Doug gets enormous satisfaction from seeing individuals, families, and businesses thrive financially. He has become a skilled negotiator with extensive experience working for a number of corporations and private firms.</p>
  <div class="abs headshot headshot--doug"><div class="headshot__photo" role="img" aria-label="Headshot of Doug Penberthy, director and licensee"></div></div>
  <p class="abs bio bio--doug-2">What differentiates Doug is his compassion and commitment to people. He works hard to be an excellent communicator with the aim of achieving great results. He has extensive sales experience with incredible ability to push the boundaries, think outside the box and meet or surpass expectations. This is why his clients keep coming back and continue to refer well into the future.</p>
  <div class="abs contact-row contact-row--doug">
    <span class="pill pill--onwhite"><span class="pill__icon"><svg width="9" height="9" viewBox="0 0 9 9"><path d="M2 .8l1.4 1.8-.8 1c.5 1 1.3 1.8 2.3 2.3l1-.8L7.7 6.5 7 8C4 8 1 5 1 2z" fill="#16202e"/></svg></span>0438 192 607</span>
    <span class="pill pill--onwhite"><span class="pill__icon"><svg width="9" height="7" viewBox="0 0 9 7"><rect x=".5" y=".5" width="8" height="6" fill="#16202e"/><path d="M.5.5L4.5 4 8.5.5" fill="none" stroke="#fff" stroke-width=".8"/></svg></span>doug@pinecrestrealestate-example.com.au</span>
  </div>

  <svg class="abs footer" viewBox="0 0 410 47"><path d="M0 0H211L236 28H410V47H0Z" fill="#16202e"/><path d="M214 0L239 25H410" stroke="#9a9ea8" stroke-width="1.5" fill="none"/></svg>
  <div class="abs footer__name">PINECREST REAL ESTATE</div>
  <div class="abs footer__contacts">
    <div><svg width="7" height="5" viewBox="0 0 7 5"><rect x=".3" y=".3" width="6.4" height="4.4" fill="none" stroke="#555" stroke-width=".6"/><path d="M.3.3L3.5 3 6.7.3" fill="none" stroke="#555" stroke-width=".6"/></svg>hello@pinecrestrealestate-example.com.au</div>
    <div><svg width="7" height="7" viewBox="0 0 7 7"><circle cx="3.5" cy="3.5" r="3" fill="none" stroke="#555" stroke-width=".6"/><path d="M.5 3.5h6M3.5.5v6" stroke="#555" stroke-width=".5"/></svg>pinecrestrealestate-example.com.au</div>
  </div>
</section>

</body>
</html>
```